Willowmere Rites Studio creates individual, personalised ceremonies to celebrate weddings, naming days,coming of age, significant age, divorce and final resting rites. Ceremonies and meaningful rituals are created in collaboration with the individual to reflect their hopes and desires, how they will/have embrace/d their lives. The final design should have the logo (purple) on a white/silver background on the right hand side of the card. Name of business and contact details in red on a black background on the left
Updates

Hi All, have only just realised I have paid for a double sided card, yep, a newbie! Sorry to set the cat amongst the pigeons but could we put 'creating...... etc' on the back?

Target Market(s)

Couples marrying, renewing of vows, baby naming days, coming of age, significant age, divorce, funeral ceremonies. The target market predominantly will be couples marrying.

Industry/Entity Type

Business

Contact Information for Business Card

Willowmere Rites Studio, Tamsin Crowther, 0492-718305 willowmereritesstudio1@quillpost.net
"Crafting singular, bespoke occasions honouring journeys"

Font styles to use
Script

Colors
eb1f27
6b449b
f3f0f8

Requirements
Must have
• On initial entry, and now, the logo was not displayed in full - the bottom part was cut off - this needs to be in it's entirety. Colours as previously specified are non-negotiable. Font and placement of characters will be assessed as produced.
Should not have
• Telephone symbol, call us, director,grammatical symbols ( : )

```html
<!DOCTYPE html>
<html lang="en">
<head>
<meta charset="utf-8">
<title>Willowmere Rites Studio – Business Card</title>
<link rel="stylesheet" href="https://fonts.googleapis.com/css2?family=Parisienne&family=Open+Sans:wght@400;700&display=swap">
<style>
  :root {
    --brand-red: #eb1f27;
    --brand-purple: #6b449b;
    --brand-lilac: #9b6fce;
    --brand-mist: #f3f0f8;
    --card-black: #0c0c0d;
    --card-white: #ffffff;
    --page-bg: #e7e4ea;
  }
  * { margin: 0; padding: 0; box-sizing: border-box; }
  html, body {
    width: 1200px;
    height: 876px;
    overflow: hidden;
    background: var(--page-bg);
  }
  .business-card {
    position: absolute;
    left: 100px;
    top: 152px;
    width: 1000px;
    height: 572px;
    background: var(--card-white);
    overflow: hidden;
    box-shadow: 0 10px 30px rgba(0,0,0,0.18);
  }
  .card-shapes {
    position: absolute;
    inset: 0;
    width: 100%;
    height: 100%;
  }
  .contact-side {
    position: absolute;
    left: 56px;
    top: 66px;
    width: 440px;
  }
  .studio-name {
    font-family: "Parisienne", cursive;
    font-weight: 400;
    color: var(--brand-red);
    font-size: 54px;
    line-height: 1.1;
  }
  .person-name {
    font-family: "Parisienne", cursive;
    color: var(--card-white);
    font-size: 48px;
    margin-top: 64px;
  }
  .phone {
    font-family: "Open Sans", sans-serif;
    font-weight: 700;
    color: var(--brand-red);
    font-size: 34px;
    letter-spacing: 1px;
    margin-top: 40px;
  }
  .email {
    font-family: "Open Sans", sans-serif;
    color: var(--brand-red);
    font-size: 18px;
    margin-top: 2px;
  }
  .brand-mark {
    position: absolute;
    left: 690px;
    top: 70px;
    width: 270px;
    display: flex;
    flex-direction: column;
    align-items: center;
    gap: 10px;
  }
  .brand-dot {
    width: 40px;
    height: 40px;
    border-radius: 50%;
    background: var(--brand-purple);
  }
  .brand-name {
    font-family: "Parisienne", cursive;
    color: var(--brand-purple);
    font-size: 38px;
    line-height: 1.15;
    text-align: center;
  }
  .tagline {
    position: absolute;
    right: 46px;
    top: 300px;
    width: 200px;
    text-align: right;
    font-family: "Parisienne", cursive;
    color: var(--brand-purple);
    font-size: 21px;
    line-height: 1.3;
  }
</style>
</head>
<body>
  <main class="business-card">
    <svg class="card-shapes" viewBox="0 0 1000 572" preserveAspectRatio="none" aria-hidden="true">
      <path class="purple-sweep" fill="var(--brand-lilac)"
            d="M560,0 C600,220 680,440 760,572 L900,572 C760,440 650,220 600,0 Z"/>
      <path class="black-panel" fill="var(--card-black)"
            d="M0,0 L560,0 C600,220 680,440 760,572 L0,572 Z"/>
    </svg>

    <section class="contact-side">
      <h1 class="studio-name">Willowmere Rites<br>Studio</h1>
      <p class="person-name">Tamsin Crowther</p>
      <p class="phone">0492-718305</p>
      <p class="email">willowmereritesstudio1@quillpost.net</p>
    </section>

    <div class="brand-mark">
      <span class="brand-dot"></span>
      <span class="brand-name">Willowmere Rites<br>Studio</span>
    </div>

    <p class="tagline">"Crafting singular, bespoke occasions honouring journeys"</p>
  </main>
</body>
</html>
```